VELINTA Promotions - Business Card Design Project

We are looking for a classy business cards for Promotion Company based in Toronto, Canada named Velinta Promotions.

Velinta Promotions has an idea and vision to set high standard, be EXCLUSIVE and attract a group of people that will follow us through events we promote (night clubs, brand promotions, music events, and sport events)

We want to present a high standards and classy image to the others...
Updates

Target Market(s)

male/female age 25-40 Target: business owners young entrepreneur - clubing industry - media industry - promotion industry - marketing media industry

Industry/Entity Type

Events

Requirements
Must have
• business cards should be classy, make people feel exclusive , make people react ..

```html
<!DOCTYPE html>
<html lang="en">
<head>
<meta charset="utf-8">
<title>Velinta Promotions – Business Card Options</title>
<link href="https://fonts.googleapis.com/css2?family=Alegreya+Sans:wght@400;500&display=swap" rel="stylesheet">
<style>
  :root {
    --page: #ffffff;
    --ink: #000000;
    --cyan: #1ab3e6;
    --paper: #ffffff;
    --text-dark: #111111;
    --frame: #9a9a9a;
    --ray-violet: #8a2aa8;
    --ray-red: #7a1a2a;
    --ray-blue: #2a2a8a;
  }
  * { margin: 0; padding: 0; box-sizing: border-box; }
  html, body { width: 1037px; height: 1200px; overflow: hidden; background: var(--page); }
  body { position: relative; font-family: "Alegreya Sans", sans-serif; }

  .card { position: absolute; width: 467px; height: 259px; overflow: hidden; background: var(--ink); }
  .col-left { left: 38px; }
  .col-right { left: 532px; }
  .row-1 { top: 40px; }
  .row-2 { top: 326px; }
  .row-3 { top: 613px; }
  .row-4 { top: 900px; }
  .card--framed { border: 1px solid var(--frame); }
  .card--paper { background: var(--paper); }

  .logo { position: absolute; left: 50px; width: 370px; color: var(--cyan); font-weight: 400; }
  .logo-name { display: block; font-size: 54px; line-height: 50px; letter-spacing: 2px; }
  .logo-tag { display: block; text-align: right; font-size: 13px; letter-spacing: 6px; line-height: 14px; padding-right: 30px; }

  .abs { position: absolute; }
  .center { left: 0; right: 0; text-align: center; }
  .name { font-size: 30px; line-height: 1; }
  .title { font-size: 11px; line-height: 1.2; }
  .contact { font-size: 12px; line-height: 14px; }
  .cyan { color: var(--cyan); }
  .white { color: var(--paper); }
  .dark { color: var(--text-dark); }
  .spaced { letter-spacing: 4px; }

  .ray-field {
    position: absolute; left: 0; width: 100%;
    background:
      radial-gradient(ellipse 18% 120% at 55% 40%, rgba(190,70,230,.85), transparent 70%),
      radial-gradient(ellipse 14% 110% at 20% 30%, rgba(150,30,60,.7), transparent 70%),
      radial-gradient(ellipse 16% 110% at 90% 40%, rgba(60,50,170,.7), transparent 70%),
      linear-gradient(90deg, #0c0410, #2a0e30 40%, #3a1046 55%, #120a28);
  }
  .band-black { position: absolute; left: 0; width: 100%; background: var(--ink); }
  .stripe-cyan { position: absolute; left: 0; width: 100%; background: var(--cyan); }
  .stripe-pattern {
    position: absolute; left: 0; width: 100%;
    background: linear-gradient(90deg, #e8e8e8, #6a6a6a 30%, #d8d8d8 55%, #555 80%, #e0e0e0);
  }
</style>
</head>
<body>

<!-- Row 1 -->
<section class="card col-left row-1">
  <div class="logo" style="top:96px"><span class="logo-name">VELINTA</span><span class="logo-tag">PROMOTIONS</span></div>
</section>

<section class="card col-right row-1">
  <div class="abs center name cyan" style="top:67px;font-size:34px">Daniel Reyes</div>
  <div class="abs center title white spaced" style="top:108px;font-size:12px">MANAGING DIRECTOR</div>
  <div class="abs center contact" style="top:142px">
    <div class="cyan">2450, Marlowe Ave., Toronto, Canada</div>
    <div class="cyan">ph.: 416 555 0192, mob.: 647 555 0148</div>
    <div class="white">inbox@velinta.com | www.velinta.com</div>
  </div>
</section>

<!-- Row 2 -->
<section class="card card--paper card--framed col-left row-2">
  <div class="band-black" style="top:0;height:130px"></div>
  <div class="logo" style="top:36px"><span class="logo-name">VELINTA</span><span class="logo-tag">PROMOTIONS</span></div>
  <div class="abs name cyan" style="left:53px;top:172px">Daniel Reyes</div>
  <div class="abs title dark" style="left:55px;top:206px">MANAGING DIRECTOR</div>
  <div class="abs contact dark" style="left:287px;top:148px">
    <div>2450, Marlowe Ave.,</div>
    <div>Toronto, Canada</div>
    <div>ph.: 416 555 0192</div>
    <div>mob.: 647 555 0148</div>
    <div>inbox@velinta.com</div>
    <div>www.velinta.com</div>
  </div>
</section>

<section class="card card--framed col-right row-2">
  <div class="ray-field" style="top:0;height:86px" role="img" aria-label="Stage light rays in violet, red and blue"></div>
  <div class="logo" style="top:96px"><span class="logo-name">VELINTA</span><span class="logo-tag">PROMOTIONS</span></div>
  <div class="abs name cyan" style="left:41px;top:190px;font-size:27px">Daniel Reyes</div>
  <div class="abs title cyan" style="left:43px;top:220px;font-size:13px">managing director</div>
  <div class="abs contact cyan" style="left:226px;top:194px;font-size:11px;line-height:12px">
    <div>2450, Marlowe Ave., Toronto, Canada</div>
    <div>ph.: 416 555 0192, mob.: 647 555 0148</div>
    <div>inbox@velinta.com | www.velinta.com</div>
  </div>
</section>

<!-- Row 3 -->
<section class="card col-left row-3">
  <div class="logo" style="top:36px"><span class="logo-name">VELINTA</span><span class="logo-tag">PROMOTIONS</span></div>
  <div class="abs center contact white" style="top:112px">
    <div>2450, Marlowe Ave., Toronto, Canada</div>
    <div>ph.: 416 555 0192, mob.: 647 555 0148</div>
    <div>inbox@velinta.com | www.velinta.com</div>
  </div>
  <div class="stripe-cyan" style="top:168px;height:24px"></div>
  <div class="abs name" style="left:33px;top:166px;color:var(--ink)">Daniel Reyes</div>
  <div class="abs title" style="left:211px;top:176px;color:var(--ink)">MANAGING DIRECTOR</div>
  <div class="stripe-pattern" style="top:192px;height:67px" role="img" aria-label="Black and white zebra stripe pattern"></div>
</section>

<section class="card card--framed col-right row-3">
  <div class="ray-field" style="top:0;height:259px" role="img" aria-label="Stage light rays in violet, red and blue"></div>
  <div class="band-black" style="top:86px;height:91px;opacity:.92"></div>
  <div class="logo" style="top:96px"><span class="logo-name">VELINTA</span><span class="logo-tag">PROMOTIONS</span></div>
  <div class="abs name white" style="left:41px;top:193px;font-size:26px">Daniel Reyes</div>
  <div class="abs title white" style="left:43px;top:222px;font-size:13px">managing director</div>
  <div class="abs contact white" style="left:226px;top:197px;font-size:11px;line-height:12px">
    <div>2450, Marlowe Ave., Toronto, Canada</div>
    <div>ph.: 416 555 0192, mob.: 647 555 0148</div>
    <div>inbox@velinta.com | www.velinta.com</div>
  </div>
</section>

<!-- Row 4 -->
<section class="card col-left row-4">
  <div class="abs center name cyan" style="top:27px;font-size:26px">Daniel Reyes</div>
  <div class="abs center title cyan" style="top:55px;font-size:13px">managing director</div>
  <div class="logo" style="top:102px"><span class="logo-name">VELINTA</span><span class="logo-tag">PROMOTIONS</span></div>
  <div class="abs center contact cyan" style="top:197px;font-size:11px;line-height:12px">
    <div>2450, Marlowe Ave., Toronto, Canada</div>
    <div>ph.: 416 555 0192, mob.: 647 555 0148</div>
    <div>inbox@velinta.com | www.velinta.com</div>
  </div>
</section>

<section class="card card--paper card--framed col-right row-4">
  <div class="band-black" style="top:85px;height:92px"></div>
  <div class="logo" style="top:96px"><span class="logo-name">VELINTA</span><span class="logo-tag">PROMOTIONS</span></div>
  <div class="abs name dark" style="left:41px;top:193px;font-size:27px">Daniel Reyes</div>
  <div class="abs title dark" style="left:43px;top:223px;font-size:13px">managing director</div>
  <div class="abs contact dark" style="left:226px;top:197px;font-size:11px;line-height:12px">
    <div>2450, Marlowe Ave., Toronto, Canada</div>
    <div>ph.: 416 555 0192, mob.: 647 555 0148</div>
    <div>inbox@velinta.com | www.velinta.com</div>
  </div>
</section>

</body>
</html>
```